Präsentationsvorlagen für Verwaltungsfirma
Zielgruppe
Verwaltungsfirma, IT-Dienstleistungen, Rechnungswesen
Aufgabenstellung
Benötigen Powerpoint Vorlage im Design unserer Farben. inkl. Logo
Benötige das Power Point Format - .pptx

```html
<!DOCTYPE html>
<html lang="de">
<head>
<meta charset="utf-8">
<title>Präsentationsvorlage – Bürogemeinschaft in Pucking</title>
<link href="https://fonts.googleapis.com/css2?family=Roboto:wght@400;700&display=swap" rel="stylesheet">
<style>
  :root {
    --page-bg: #ffffff;
    --slide-bg: #ffffff;
    --brand-blue: #1a6fc0;
    --brand-navy: #1d4fa3;
    --accent-blue: #2262d8;
    --text-main: #1c1c1c;
  }
  html, body {
    margin: 0;
    width: 1200px;
    height: 1200px;
    overflow: hidden;
    background: var(--page-bg);
    font-family: "Roboto", Arial, sans-serif;
  }
  .canvas { position: relative; width: 1200px; height: 1200px; }
  .slide {
    position: absolute;
    left: 203px;
    width: 808px;
    height: 454px;
    background: var(--slide-bg);
    box-shadow: 0 8px 16px rgba(0,0,0,0.18);
    overflow: hidden;
  }
  .slide--interior { top: 116px; }
  .slide--exterior { top: 644px; }
  .slide__title {
    position: absolute;
    left: 28px;
    top: 44px;
    margin: 0;
    font-size: 31px;
    font-weight: 700;
    color: var(--brand-blue);
    letter-spacing: -0.2px;
    white-space: nowrap;
  }
  .slide__body {
    position: absolute;
    left: 28px;
    top: 128px;
    width: 305px;
    margin: 0;
    font-size: 15px;
    line-height: 18.2px;
    color: var(--text-main);
  }
  .slide__brand {
    position: absolute;
    left: 28px;
    top: 404px;
    font-size: 22px;
    font-weight: 400;
    color: var(--brand-navy);
    white-space: nowrap;
  }
  .photo { position: absolute; }
  .photo--meeting {
    left: 484px; top: 0; width: 324px; height: 209px;
    background: linear-gradient(160deg, #b9c7c4 0%, #6f8a6a 40%, #8a5a35 70%, #2a3446 100%);
  }
  .photo--kitchen {
    left: 484px; top: 210px; width: 180px; height: 244px;
    background: linear-gradient(170deg, #e8e4dc 0%, #c9a57a 50%, #3a2f28 100%);
  }
  .photo--stairs {
    left: 665px; top: 210px; width: 143px; height: 244px;
    background: linear-gradient(170deg, #e4e4e0 0%, #b9b7ae 55%, #777a78 100%);
  }
  .photo--aerial {
    left: 484px; top: 0; width: 324px; height: 454px;
    background: linear-gradient(180deg, #9fc3e2 0%, #4f7a3a 22%, #5f7a62 38%, #3f5a2e 50%, #6b6f78 62%, #2a66d8 78%, #5d7040 100%);
  }
  .slide__accent {
    position: absolute;
    left: 484px;
    bottom: 0;
    width: 324px;
    height: 10px;
    background: var(--accent-blue);
  }
</style>
</head>
<body>
<div class="canvas">

  <section class="slide slide--interior">
    <div class="photo photo--meeting" role="img" aria-label="Foto: heller Besprechungsraum mit großem Holztisch und Fensterfront"></div>
    <div class="photo photo--kitchen" role="img" aria-label="Foto: moderne Büroküche mit Theke und Barhockern"></div>
    <div class="photo photo--stairs" role="img" aria-label="Foto: Treppenaufgang mit Metallgeländer und Pflanzen"></div>
    <div class="slide__accent"></div>
    <h1 class="slide__title">Bürogemeinschaft in Pucking</h1>
    <p class="slide__body">Wir, die Nordwerk &amp; Kollegen Verwaltung GmbH, sind eine renommierte Firmengruppe in Pucking (Linz-Land) und bieten neben der Gebäudeverwaltung eine Vielzahl zentraler Dienstleistungen an diesem Standort an. Mit unserem umfangreichen Leistungsspektrum tragen wir dazu bei, die Geschäftsprozesse unserer Kund:innen reibungslos und effizient zu gestalten.</p>
    <div class="slide__brand">Nordwerk &amp; Kollegen</div>
  </section>

  <section class="slide slide--exterior">
    <div class="photo photo--aerial" role="img" aria-label="Luftbild: Bürogebäude mit blauer Fassade und Solardach an einem See"></div>
    <div class="slide__accent"></div>
    <h1 class="slide__title">Bürogemeinschaft in Pucking</h1>
    <p class="slide__body">Wir, die Nordwerk &amp; Kollegen Verwaltung GmbH, sind eine renommierte Firmengruppe in Pucking (Linz-Land) und bieten neben der Gebäudeverwaltung eine Vielzahl zentraler Dienstleistungen an diesem Standort an. Mit unserem umfangreichen Leistungsspektrum tragen wir dazu bei, die Geschäftsprozesse unserer Kund:innen reibungslos und effizient zu gestalten.</p>
    <div class="slide__brand">Nordwerk &amp; Kollegen</div>
  </section>

</div>
</body>
</html>
```